Flyer redesign

We need this flier {Seasonal Care back 2018} redesigned for our 2019 season. It is attached below. New design should look different from current design. Be creative yet still professional.

Requirements
Must have
• Designed in photoshop.
• Should have the same text as current design. Only is "2019" instead of 2018. We want a different look with same info to send our customers next year.
• size: standard letter paper 8.5" x 11"
Nice to have
• Can use optional images provided. Not required though. See our website for more photos. hollowbrookgardens.org. send message through sketchwharf if you want a specific photo.
Should not have
• Do not take current design and just change date or image. Make the design look different.

```html
<!DOCTYPE html>
<html lang="en">
<head>
<meta charset="utf-8">
<title>Hollowbrook Cemetery – 2019 Gravesite Landscaping Packages</title>
<link rel="stylesheet" href="https://fonts.googleapis.com/css2?family=Roboto+Condensed:wght@400;700&family=Montserrat:wght@700;800&family=Roboto:wght@400;700&display=swap">
<style>
  :root {
    --maroon: #7a1f2e;
    --maroon-text: #8c2432;
    --blush: #e6d3d7;
    --ink: #3a3a3a;
    --footer: #565656;
    --gold: #f3b41c;
    --card-top: #ffffff;
    --card-bottom: #dcdcdc;
  }
  * { margin: 0; padding: 0; box-sizing: border-box; }
  html, body { width: 927px; height: 1200px; overflow: hidden; background: #fff; }
  .flyer { position: relative; width: 927px; height: 1200px; overflow: hidden; background: #f2f2f2; font-family: "Roboto Condensed", sans-serif; color: var(--ink); }

  .top-band { position: absolute; top: 0; left: 0; width: 927px; height: 28px; background: var(--maroon); }
  .top-band .tab { position: absolute; left: 62px; width: 328px; height: 28px; background: var(--blush); }

  .hero-photo { position: absolute; top: 28px; left: 0; width: 927px; height: 744px;
    background:
      linear-gradient(180deg, rgba(255,255,255,0) 78%, #f2f2f2 100%),
      radial-gradient(ellipse at 55% 75%, #8a8f86 0%, rgba(138,143,134,0) 35%),
      linear-gradient(180deg, #e7efe0 0%, #5f8a3a 22%, #3f6b2a 45%, #7aa34a 68%, #b9c3b0 80%, #9ea89a 100%); }

  .header { position: absolute; top: 28px; left: 0; width: 927px; height: 96px; background: rgba(255,255,255,0.82); }
  .logo-box { position: absolute; top: 28px; left: 62px; width: 328px; height: 100px; background: #fff; border-radius: 0 0 40px 40px / 0 0 20px 20px; display: flex; align-items: center; justify-content: center; }
  .logo-name { font-family: "Roboto Condensed", sans-serif; font-weight: 400; font-size: 22px; color: var(--ink); letter-spacing: 1px; }

  .title { position: absolute; top: 62px; left: 410px; white-space: nowrap; color: var(--maroon); font-weight: 400; font-size: 24px; letter-spacing: 0.2px; }
  .title .year { font-weight: 700; font-size: 32px; margin-right: 4px; }

  .card { position: absolute; width: 250px; background: linear-gradient(180deg, var(--card-top) 0%, #f3f3f3 45%, var(--card-bottom) 100%); border-radius: 6px; box-shadow: 6px 8px 12px rgba(0,0,0,0.35); overflow: hidden; }
  .card-head { background: var(--maroon); color: #fff; font-family: "Roboto", sans-serif; font-weight: 400; font-size: 21px; line-height: 20px; text-align: center; display: flex; align-items: center; justify-content: center; }
  .card-body { padding: 18px 32px 0 27px; }
  .lead { color: var(--maroon-text); font-weight: 700; font-size: 16px; line-height: 21px; margin-bottom: 12px; }
  .perks { list-style: none; font-size: 14px; line-height: 18.4px; }
  .perks li { margin-bottom: 12px; }
  .perks li::before { content: "\2022"; margin-right: 2px; }

  .price-label { font-family: "Montserrat", sans-serif; font-weight: 700; color: var(--maroon-text); font-size: 16px; line-height: 20px; text-align: center; letter-spacing: 0.5px; }
  .price { font-family: "Montserrat", sans-serif; font-weight: 800; color: var(--maroon-text); text-align: center; font-size: 36px; line-height: 40px; }
  .note { font-size: 11px; line-height: 14.5px; text-align: center; color: var(--ink); }

  .seasonal { left: 62px; top: 702px; height: 422px; }
  .seasonal .card-head { height: 60px; }
  .seasonal .card-body { padding-top: 20px; padding-right: 34px; }
  .seasonal .pricing { position: absolute; left: 0; right: 0; top: 250px; }
  .seasonal .terms { display: flex; justify-content: center; margin-top: 8px; }
  .seasonal .term { width: 96px; }
  .seasonal .term + .term { border-left: 1px solid var(--maroon); }
  .seasonal .note { position: absolute; left: 0; right: 0; bottom: 14px; }

  .basic { left: 342px; top: 669px; height: 455px; }
  .basic .card-head { height: 61px; padding-top: 4px; }
  .basic .pricing { position: absolute; left: 0; right: 0; top: 306px; }
  .basic .note { position: absolute; left: 20px; right: 20px; bottom: 16px; }

  .perpetual { left: 622px; top: 594px; height: 530px; }
  .perpetual .card-head { height: 61px; }
  .perpetual .card-body { padding: 14px 18px 0 16px; }
  .perpetual .lead { margin-bottom: 16px; }
  .perpetual .perks li { margin-bottom: 13px; }
  .perpetual .pricing { position: absolute; left: 0; right: 0; top: 381px; }
  .perpetual .note { position: absolute; left: 20px; right: 20px; bottom: 36px; }

  .badge { position: absolute; left: 822px; top: 534px; width: 82px; height: 82px; }
  .badge-text { position: absolute; left: 822px; top: 561px; width: 82px; text-align: center; font-family: "Roboto", sans-serif; font-weight: 700; font-size: 11.5px; line-height: 14px; color: var(--maroon); }

  .footer { position: absolute; left: 0; top: 1140px; width: 927px; height: 60px; background: var(--footer); display: flex; align-items: center; color: #fff; font-family: "Roboto", sans-serif; font-size: 22px; }
  .footer .item { text-align: center; }
  .footer .email { width: 357px; }
  .footer .phone { width: 219px; font-weight: 700; }
  .footer .web { width: 351px; }
  .footer .divider { width: 2px; height: 42px; background: var(--maroon); }
</style>
</head>
<body>
<main class="flyer">
  <div class="hero-photo" role="img" aria-label="Photograph of a tree-lined cemetery lane with headstones and trimmed boxwood hedges"></div>
  <div class="top-band"><div class="tab"></div></div>
  <div class="header"></div>
  <div class="logo-box"><span class="logo-name">Hollowbrook Cemetery</span></div>
  <h1 class="title"><span class="year">2019</span> GRAVESITE LANDSCAPING PACKAGES</h1>

  <section class="card seasonal">
    <h2 class="card-head">SEASONAL CARE</h2>
    <div class="card-body">
      <p class="lead">Seasonal Landscaping<br>grave care</p>
      <ul class="perks">
        <li>Weeding and trimming services on your gravesite approximately every 7 weeks during the growing season: mid-April through mid-October</li>
      </ul>
    </div>
    <div class="pricing">
      <p class="price-label">1 YEAR</p>
      <p class="price">$109</p>
      <div class="terms">
        <div class="term"><p class="price-label">2 YEARS</p><p class="price">$218</p></div>
        <div class="term"><p class="price-label">3 YEARS</p><p class="price">$327</p></div>
      </div>
    </div>
    <p class="note">Multi-year payment locks in current rates.</p>
  </section>

  <section class="card basic">
    <h2 class="card-head">BASIC CARE<br>ENDOWMENT</h2>
    <div class="card-body">
      <p class="lead">Landscaping care forever for graves with no plantings.</p>
      <ul class="perks">
        <li>Weeding and trimming services on your gravesite 2 times per year: mid-May and mid-September</li>
        <li>Monument leveling</li>
        <li>Payment ensures grave care forever</li>
      </ul>
    </div>
    <div class="pricing">
      <p class="price-label">12 MONTHLY<br>PAYMENTS OF</p>
      <p class="price">$225.00</p>
    </div>
    <p class="note">*gravesites with single headstones.<br>Call for the monument types d single<br>payment discount. Valid through 10/31/18.</p>
  </section>

  <section class="card perpetual">
    <h2 class="card-head">PERPETUAL CARE<br>ENDOWMENT</h2>
    <div class="card-body">
      <p class="lead">Landscaping care forever for graves with plantings.</p>
      <ul class="perks">
        <li>Weeding and trimming services on your gravesite approximately every 7 weeks during the growing season: mid-April through mid-October</li>
        <li>Monument leveling and cleaning</li>
        <li>Payment ensures grave care forever</li>
        <li>Full bed of boxwood shrubs Replacement of shrubs</li>
        <li>Trust certificate</li>
      </ul>
    </div>
    <div class="pricing">
      <p class="price-label">12 MONTHLY<br>PAYMENTS OF</p>
      <p class="price">$280.42</p>
    </div>
    <p class="note">Call for single payment discount.<br>Valid through 10/31/18.</p>
  </section>

  <svg class="badge" viewBox="0 0 100 100" aria-hidden="true">
    <polygon fill="var(--gold)" points="50,2 57,13 69,6 71,20 85,18 81,31 95,35 85,45 95,55 81,62 85,76 71,75 69,90 57,82 50,96 43,82 31,90 29,75 15,76 19,62 5,55 15,45 5,35 19,31 15,18 29,20 31,6 43,13"/>
    <circle cx="50" cy="49" r="33" fill="#f8c63a"/>
  </svg>
  <p class="badge-text">MOST<br>POPULAR</p>

  <footer class="footer">
    <span class="item email">info@hollowbrookgardens.org</span>
    <span class="divider"></span>
    <span class="item phone">(201) 555-0148</span>
    <span class="divider"></span>
    <span class="item web">www.hollowbrookgardens.org</span>
  </footer>
</main>
</body>
</html>
```